Coral Wing Flights brochure

A single A4 brochures that is tri-folded and shows some of our tour packages with contact details.

Please visit www.coralwingflights.com.au to see the designs and images that can be used.

I want to provide designers the freedom to try something creative because I want to give prospective client - normally tourists to Sydney a quality service. I want the brochure to reflect this.

The image on the front page needs to be of the Sydney Harbour. The image MUST be in daylight - not night time.

I have now provided an image of the aircraft (in GIF format). Please use this image and place it over the image of the harbour arch crossing and harbourside concert hall.

I may need to discuss this further but what I have not show in the attached files is a small form I will like the client to fill out..

Reservation number
Name
Address
Phone number
Email

We can discuss this at a latter time.

The QR Code needs to contain your web address (www.coralwingflights.com.au)

Target Market(s)

Visitors and tourists to Sydney who want a day trip.
We are providing an exciting way to see Sydney. By air in a light aircraft...

Industry/Entity Type

House

Font styles to use
Sans Serif
Script

Colors
33a6d7
3276b5
85acd3
85cae6
ffffff

Requirements
Must have
• Brochure must be A4 (with about 2 to 3mm bleed - so it can be cut at the printers). They but be folded in 3 to produce a DL size brochure.

The words "Prepare to be amazed" should be in script font...

Please use the following wording for our Terms can conditions...

Terms and Conditions
Coral Wing Flights operates from Pellham Field within Sydney’s busy airspace Your chosen flight may be subject to delays. Clearance to enter controlled airspace may be refused - this is especially true of our popular Coastline Panorama flight. If this happens, we can either offer other suitable flights, reschedule the flight or, if this isn’t suitable, we provide a refund.
Other aircraft, besides our standard Falcor Trekkers, are available if we consider they better suit your requirements.
See our web site www.coralwingflights.com.au for full details.
Coral Wing Flights is a trading name of Brightmere Pty Limited
(ABN 71 408 226 519) which operates under the Air Operators Certificate (AOC) of Durrow and Fitzgale Pty Ltd.
Nice to have
• Suggestion - on one of the sides (with the packages) to have a background image.

Suggestion is to keep the brochure light and "airy"

```html
<!DOCTYPE html>
<html lang="en">
<head>
<meta charset="utf-8">
<title>Coral Wing Flights – Tour Packages</title>
<link rel="stylesheet" href="https://fonts.googleapis.com/css2?family=Libre+Baskerville:wght@700&family=Sorts+Mill+Goudy&display=swap">
<style>
  :root {
    --brand-deep: #3276b5;
    --brand-sky: #33a6d7;
    --brand-soft: #85acd3;
    --brand-pale: #85cae6;
    --paper: #ffffff;
    --body-ink: #4479b8;
    --fact-ink: #4f82c0;
  }
  * { margin: 0; padding: 0; box-sizing: border-box; }
  html, body { width: 1200px; height: 849px; overflow: hidden; background: var(--paper); }
  body { font-family: "Sorts Mill Goudy", Georgia, serif; color: var(--body-ink); }

  .spread { position: relative; width: 1200px; height: 849px; }
  .panel { position: absolute; top: 0; width: 400px; height: 849px; text-align: center; }
  .panel--harbour { left: 0; }
  .panel--coastal { left: 400px; }
  .panel--mountains { left: 800px; }

  .photo-frame {
    position: absolute; top: 32px; left: 32px; width: 336px; height: 209px;
    border: 8px solid var(--brand-deep); background: var(--brand-deep);
  }
  .photo { width: 100%; height: 100%; }
  .photo--harbour { background: linear-gradient(180deg, #b7c1c6 0%, #5c7886 100%); }
  .photo--coastal { background: linear-gradient(180deg, #a5c4e2 0%, #55683f 100%); }
  .photo--mountains { background: linear-gradient(180deg, #c8b6c6 0%, #4e6535 100%); }

  .tour-title { position: absolute; left: 0; right: 0; top: 251px; padding: 0 16px; }
  .tour-title h2 {
    font-family: "Libre Baskerville", Georgia, serif;
    font-size: 16.5px; font-weight: 700; color: var(--brand-deep); line-height: 20px;
  }
  .tour-title .tagline {
    font-family: "Libre Baskerville", Georgia, serif;
    font-size: 10.6px; font-weight: 700; color: var(--brand-deep); line-height: 14.5px;
  }
  .tour-title .fact { font-size: 13.5px; color: var(--fact-ink); line-height: 14.6px; }

  .features { position: absolute; left: 28px; right: 28px; top: 382px; }
  .panel--mountains .features { left: 30px; right: 30px; }
  .feature { margin-bottom: 11px; font-size: 10.4px; line-height: 11.5px; }
  .feature h3 {
    font-family: "Libre Baskerville", Georgia, serif;
    font-size: 9px; font-weight: 700; color: var(--brand-deep); line-height: 12px;
  }

  .mission { position: absolute; left: 70px; right: 70px; top: 720px; }
  .mission svg { display: block; width: 260px; height: 6px; margin: 0 auto; }
  .mission p {
    font-family: "Libre Baskerville", Georgia, serif;
    font-size: 14px; font-weight: 700; color: var(--brand-deep); line-height: 19.5px; padding: 8px 0 7px;
  }
</style>
</head>
<body>
<main class="spread">

  <section class="panel panel--harbour">
    <div class="photo-frame"><div class="photo photo--harbour" role="img" aria-label="Aerial daylight photo of the harbour with the harbour arch crossing and harbourside concert hall"></div></div>
    <header class="tour-title">
      <h2>Sydney Harbour Scenic</h2>
      <p class="tagline">Spectacular views of world famous Sydney Harbour<br>and harbourside concert hall by air</p>
      <p class="fact">Duration: 1 hour 20 mins</p>
      <p class="fact">Location: Pellham Field</p>
      <p class="fact">Price: $560 per aircraft</p>
    </header>
    <div class="features">
      <div class="feature"><h3>Feature 1</h3><p>Arrive at Pellham Field. After you make your way to Pellham Field, you will be greeted by one of our friendly staff who will give you a brief of the flight. Tea and coffee will be served. Should you prefer we can arrange transport at additional cost.</p></div>
      <div class="feature"><h3>Feature 2</h3><p>Parramatta City. Soon after take-off we head north to fly over Parramatta City at about 2000 feet.</p></div>
      <div class="feature"><h3>Feature 3</h3><p>Hornsby. Flying further north we arrive over Hornsby – a suburb on the Upper North Shore. Hornsby is located 25 kilometres north-west of Sydney’s CBD.</p></div>
      <div class="feature"><h3>Feature 4</h3><p>Overfly the Bahai Temple. Heading further east we arrive over this prominent land-mark near Sydney’s Northern Beaches.</p></div>
      <div class="feature"><h3>Feature 5</h3><p>Long Reef. Having flown over Narrabeen and Collaroy Beaches – some of Sydney’s most lovely coastal playgrounds, we arrive over Long Reef. Long Reef is a headland that sits between Collaroy Beach and Dee Why Beach.</p></div>
      <div class="feature"><h3>Feature 6</h3><p>Famous Sydney Harbour. We arrive over one of the worlds most recognisable and spectacular sights – Sydney Harbour.</p></div>
      <div class="feature"><h3>Feature 7</h3><p>Manly Beach. But we are not done yet! After leaving Sydney Harbour, we fly over both South Head and North Head which guards the entrance to Sydney Harbour and we make our way to Manly Beach.</p></div>
      <div class="feature"><h3>Feature 8</h3><p>Back home. Upon your arrival back at Pellham Field, you can celebrate your Sydney Tour with a glass of sparkling wine – or other refreshing beverages that takes your fancy.</p></div>
    </div>
  </section>

  <section class="panel panel--coastal">
    <div class="photo-frame"><div class="photo photo--coastal" role="img" aria-label="Photo of sandstone coastal cliffs with a lighthouse and the city skyline behind"></div></div>
    <header class="tour-title">
      <h2>Sydney Coastal</h2>
      <p class="tagline">A popular Sydney tour showcasing<br>famous Sydney beaches and amazing coastline.</p>
      <p class="fact">Duration: 1 hour 20 mins</p>
      <p class="fact">Location: Pellham Field</p>
      <p class="fact">Price: $560 per aircraft</p>
    </header>
    <div class="features">
      <div class="feature"><h3>Feature 1</h3><p>Arrive at Pellham Field. After you make your way to Pellham Field, you will be greeted by one of our friendly staff who will give you a brief of the flight. Tea and coffee will be served. Should you prefer we can arrange transport at additional cost.</p></div>
      <div class="feature"><h3>Feature 2</h3><p>Campbelltown. Soon after take-off we head south to fly over the historic city of Campbelltown.</p></div>
      <div class="feature"><h3>Feature 3</h3><p>Stanwell Park. This area was originally inhabited by the Wadi Wadi Aboriginal group. Stanwell Park is a picturesque coastal village and northern suburb of Wollongong.</p></div>
      <div class="feature"><h3>Feature 4</h3><p>Jibbon Point &amp; Port Hacking. Jibbon Point marks the southern side of the entrance to Port Hacking.</p></div>
      <div class="feature"><h3>Feature 5</h3><p>Sydney Beaches. With the coastline on the left side of the aircraft, we now fly north and view some of Sydney’s most famous beaches.</p></div>
      <div class="feature"><h3>Feature 6</h3><p>Sydney Heads. Between the beaches of Tamarama and Manly, your pilot will fly you over Sydney Heads. This is the entrance to Sydney Harbour where you can get a fantastic view of the harbour with Sydney City in the background.</p></div>
      <div class="feature"><h3>Feature 7</h3><p>Long Reef. Having flown over some of Sydney’s most lovely coastline and beaches, we arrive over Long Reef. Long Reef is a headland that sits between Collaroy Beach and Dee Why Beach.</p></div>
      <div class="feature"><h3>Feature 8</h3><p>Back home. Upon your arrival back at Pellham Field, you can celebrate your Sydney Coastal Tour with a glass of sparkling wine – or other refreshing beverages that takes your fancy.</p></div>
    </div>
  </section>

  <section class="panel panel--mountains">
    <div class="photo-frame"><div class="photo photo--mountains" role="img" aria-label="Photo of the Three Sisters rock formation above forested valleys"></div></div>
    <header class="tour-title">
      <h2>The Blue Mountains, the Three Sisters,<br>&amp; Warragamba Dam</h2>
      <p class="tagline">Sydney's spectacular west. The Blue Mountains<br>in all its glory.</p>
      <p class="fact">Duration: 1 hour 10 mins</p>
      <p class="fact">Location: Pellham Field</p>
      <p class="fact">Price: $475 per aircraft</p>
    </header>
    <div class="features">
      <div class="feature"><h3>Feature 1</h3><p>Arrive at Pellham Field. After you make your way to Pellham Field, you will be greeted by one of our friendly staff who will give you a brief of the flight. Tea and coffee will be served. Should you prefer we can arrange transport at additional cost.</p></div>
      <div class="feature"><h3>Feature 2</h3><p>The Blue Mountains, Katoomba, and the Three Sisters. Shortly after take-off your pilot will steer a westerly heading and track direct to Katoomba and the famous Three Sisters. The Three Sisters is the Blue Mountains’ (ask your pilot why they are called the Blue Mountains) most spectacular landmark. Located at Echo Point Katoomba is an iconic visitor attraction and is experienced by millions of people each year. The Three Sisters is essentially an unusual rock formation representing three sisters who according to Aboriginal legend were turned to stone.</p></div>
      <div class="feature"><h3>Feature 3</h3><p>Warragamba Dam. This important resource supplies water to more than 3.7 million people living in Sydney and the lower Blue Mountains.</p></div>
      <div class="feature"><h3>Feature 4</h3><p>Back home. Upon your return to Pellham Field, you can celebrate your Blue Mountains tour with a glass of sparkling wine – or other refreshing beverage that takes your fancy. We will have some delicious snacks ready for you to enjoy and hopefully cap off a memorable day.</p></div>
    </div>
    <div class="mission">
      <svg viewBox="0 0 260 6" aria-hidden="true"><path d="M0 3 Q130 0 260 3 Q130 5 0 3Z" fill="var(--brand-deep)"/></svg>
      <p>Our mission is to make your flight over Sydney a memorable and happy experience.</p>
      <svg viewBox="0 0 260 6" aria-hidden="true"><path d="M0 3 Q130 0 260 3 Q130 5 0 3Z" fill="var(--brand-deep)"/></svg>
    </div>
  </section>

</main>
</body>
</html>
```